Fresh look for Client Documents

We have a new software system and it now generates word document reports. We need these tidied up and consistently branded with a stylish corporate theme. We also need to add a "powered by Brimquell" theme to them as the reports are generated by business that use the software so the documents do not exactly 'belong' to their brand. On all of them we need to have the powred by Brimquell PLUS provision for a businesses own logo.
All the documents are generated in Word

```html
<!DOCTYPE html>
<html lang="en">
<head>
<meta charset="utf-8">
<title>Brimquell Client Document Templates</title>
<link href="https://fonts.googleapis.com/css2?family=Carlito:ital,wght@0,400;0,700;1,400&display=swap" rel="stylesheet">
<style>
  :root {
    --backdrop: #b0b0b0;
    --paper: #ffffff;
    --ink: #1a1a1a;
    --brand: #8193bd;
    --band: #94a0b8;
    --divider: #d6def0;
    --logo-slot: #eef1f7;
    --muted: #666a72;
    --highlight: #ffff00;
    --note: #e00000;
    --rule: #000000;
    --soft-rule: #e2e2e2;
  }
  * { margin: 0; padding: 0; box-sizing: border-box; }
  html, body { width: 1200px; height: 1114px; overflow: hidden; }
  body {
    background: var(--backdrop);
    font-family: "Carlito", "Calibri", sans-serif;
    color: var(--ink);
    position: relative;
  }
  .page {
    position: absolute;
    background: var(--paper);
    width: 351px;
    height: 494px;
  }
  .page-template { left: 54px; top: 58px; width: 350px; }
  .page-workorder { left: 424px; top: 60px; }
  .page-audit { left: 796px; top: 57px; height: 498px; }
  .page-summary { left: 54px; top: 576px; height: 495px; }
  .page-insurance { left: 424px; top: 576px; height: 498px; }

  .band {
    position: absolute; left: 0; right: 0; bottom: 0; height: 12px;
    background: var(--band);
  }

  /* Space reserved for the issuing business's own logo */
  .client-logo-slot {
    position: absolute;
    left: 40px; top: 20px; width: 59px; height: 39px;
    background: linear-gradient(180deg, var(--logo-slot), #e4e9f3);
  }
  .client-logo-slot-audit { left: 25px; top: 13px; width: 66px; height: 44px; }
  .client-logo-slot-lg { left: 42px; top: 7px; width: 82px; height: 55px; }

  .brand {
    display: flex; align-items: center; gap: 4px;
    color: var(--brand);
    font-weight: 400;
    letter-spacing: 0.3px;
    white-space: nowrap;
  }
  .brand-mark { width: 6px; height: 6px; background: var(--brand); }

  .powered {
    position: absolute; display: flex; align-items: center; gap: 14px;
  }
  .powered-label { font-size: 6.5px; color: var(--muted); }
  .powered .brand { font-size: 8px; }

  .line {
    position: absolute; left: 42px;
    font-size: 5.6px; line-height: 1; white-space: nowrap; font-weight: 400;
  }
  .title {
    position: absolute; left: 42px;
    font-weight: 400; white-space: nowrap; line-height: 1;
  }

  /* Inspection template */
  .inspection-table {
    position: absolute; left: 40px; top: 92px; width: 268px;
    border-collapse: collapse; table-layout: fixed;
    font-size: 5.6px; line-height: 1.3;
  }
  .inspection-table td {
    border: 0.8px solid var(--rule);
    vertical-align: top; padding: 0.5px 3.5px;
  }
  .inspection-table .check { text-align: center; }

  /* Work order */
  .building-grid { position: absolute; left: 42px; font-size: 5.4px; }
  .building-grid span { position: absolute; white-space: nowrap; }
  .order-table {
    position: absolute; left: 41.5px; top: 213px; width: 290.5px;
    border-collapse: collapse; table-layout: fixed; font-size: 5.2px;
  }
  .order-table td {
    border: 0.8px solid var(--rule); padding: 0 3px; vertical-align: top; line-height: 1.3;
  }
  .qr-list {
    position: absolute; left: 41.5px; top: 357px; width: 129px;
    border-collapse: collapse; font-size: 6.9px; line-height: 1.3;
    font-weight: 400; color: #222;
  }
  .qr-list td { border: 0.6px solid var(--soft-rule); padding: 0 1px; font-weight: 400; }

  /* Audit */
  .audit-note {
    position: absolute; left: 41.5px; top: 162px; width: 268px;
    font-size: 5.5px; font-style: italic; text-align: justify; line-height: 1.55;
  }
  .b { font-weight: 700; }
  .fine { font-size: 3.4px; font-style: italic; font-weight: 400; }
  .portfolio-divider {
    position: absolute; left: 41px; top: 325px; width: 269px; height: 8px;
    background: var(--divider);
  }
  .mark { background: var(--highlight); }
  .note-red { color: var(--note); }
</style>
</head>
<body>

<!-- Inspection checklist template -->
<section class="page page-template">
  <div class="client-logo-slot" role="img" aria-label="Space for the business's own logo"></div>
  <table class="inspection-table">
    <colgroup>
      <col style="width:67.5px"><col style="width:47px"><col style="width:40px"><col style="width:23px"><col style="width:32.5px"><col style="width:23px"><col style="width:35px">
    </colgroup>
    <tr style="height:24px"><td colspan="7">Building Name<br>Building Address<br>Management Group</td></tr>
    <tr style="height:16px"><td></td><td></td><td>Defect Observed?</td><td>Minor</td><td>Moderate</td><td>Major</td><td>Comments</td></tr>
    <tr style="height:8px"><td>Area</td><td>Item</td><td class="check">☑</td><td class="check">☑</td><td class="check">☑</td><td class="check">☑</td><td></td></tr>
    <tr style="height:24.5px"><td>Basement &amp; Internal Car Accommodation</td><td>Kerbs and line marking (repaint)</td><td></td><td></td><td></td><td></td><td></td></tr>
    <tr style="height:16.3px"><td></td><td>Gas detection Unit</td><td></td><td></td><td></td><td></td><td></td></tr>
    <tr style="height:16.3px"><td></td><td>Roller shutter doors</td><td></td><td></td><td></td><td></td><td></td></tr>
    <tr style="height:16.3px"><td></td><td>Motion Sensors</td><td></td><td></td><td></td><td></td><td></td></tr>
    <tr style="height:16.3px"><td></td><td>Driveway</td><td></td><td></td><td></td><td></td><td></td></tr>
    <tr style="height:16.3px"><td>Bathrooms &amp; Toilets</td><td>Joinery</td><td></td><td></td><td></td><td></td><td></td></tr>
    <tr style="height:16.3px"><td></td><td>Toilet</td><td></td><td></td><td></td><td></td><td></td></tr>
    <tr style="height:15.7px"><td>Elevator</td><td></td><td></td><td></td><td></td><td></td><td></td></tr>
  </table>
  <div class="powered" style="left:223px; top:451px;"><span class="powered-label">Powered by</span><span class="brand"><span class="brand-mark"></span>BRIMQUELL</span></div>
  <div class="band"></div>
</section>

<!-- Contractor work order -->
<section class="page page-workorder">
  <div class="client-logo-slot" role="img" aria-label="Space for the business's own logo"></div>
  <div class="line" style="top:84px">Management Group: Harbour Realty</div>
  <div class="line" style="top:92.5px">Strata Manager: Mara Quinn</div>
  <div class="line" style="top:108px">Building details:</div>
  <div class="line" style="top:116px">Bayview</div>
  <div class="line" style="top:124px">22 Tallow Street Ashby ACT</div>
  <div class="line" style="top:132px">Approximate Build Date 2016, Heritage Listed? No</div>
  <div class="building-grid" style="top:140px">
    <span style="left:0">No. of Commercial Lots 2</span>
    <span style="left:85px">Retail☑</span>
    <span style="left:121px">Commercial/Office</span>
    <span style="left:192px">Industrial</span>
  </div>
  <div class="building-grid" style="top:156px">
    <span style="left:0">Storeys 3</span><span style="left:43px">Basement 2</span><span style="left:85px">Lifts 4</span><span style="left:149px">Escalator 0</span>
  </div>
  <div class="building-grid" style="top:164px">
    <span style="left:0">Pool 1</span><span style="left:43px">Spa 0</span><span style="left:85px">Sauna 0</span><span style="left:149px">Steam Room 0</span>
  </div>
  <div class="building-grid" style="top:172px">
    <span style="left:0">Gym 1</span><span style="left:43px">Tennis Court 1</span><span style="left:85px">Playground 0</span><span style="left:149px">BBQ 3</span>
  </div>
  <h2 class="title" style="top:197px; font-size:13px;">Contractor Work Order</h2>
  <table class="order-table">
    <colgroup><col style="width:88.5px"><col></colgroup>
    <tr style="height:7.8px"><td>Area</td><td>Superstructure</td></tr>
    <tr style="height:9px"><td>Asset</td><td>Building Membrane</td></tr>
    <tr style="height:94.5px"><td>Strata Manager Comments</td><td></td></tr>
  </table>
  <div class="line" style="top:337px">QR Codes have been installed at the following locations in this building. It is a requirement that all</div>
  <div class="line" style="top:344.5px">service technicians check in on arrival.</div>
  <table class="qr-list">
    <tr><td>Fire Indicator Panel - Building One</td></tr>
    <tr><td>Pedestrian Access Door Two - Main Level Carpark</td></tr>
    <tr><td>Pedestrian Access Door One - Main Level Carpark</td></tr>
    <tr><td>Main Level Carpark - Notice Board Two</td></tr>
    <tr><td>Main Level Carpark - Notice Board One</td></tr>
  </table>
  <div class="powered" style="left:223px; top:451px;"><span class="powered-label">Powered by</span><span class="brand"><span class="brand-mark"></span>BRIMQUELL</span></div>
  <div class="band"></div>
</section>

<!-- Management audit report -->
<section class="page page-audit">
  <div class="client-logo-slot client-logo-slot-audit" role="img" aria-label="Space for the business's own logo"></div>
  <h1 class="title" style="top:72px; left:41.5px; font-size:14.5px;">Management Audit Report</h1>
  <div class="line" style="left:41.5px; top:95px">Prepared for: [[Strata Management Group]]</div>
  <div class="line" style="left:41.5px; top:108px">Date Generated: [[Today’s Date]]</div>
  <div class="line" style="left:41.5px; top:122px">Reporting Period: [[Date from]] – [[Date to]]</div>
  <div class="line" style="left:41.5px; top:135px">Number of [[Strata Management Group]] buildings using Brimquell = [[total buildings for the group]]</div>
  <p class="audit-note">The following log shows all Brimquell activity for [[Strata Management Group]] Users during the selected reporting period. Note if more than one Strata Manager is recorded as a User against a building, the building results will be duplicated in the individual portfolios presented below.</p>

  <div class="line" style="left:41.5px; top:206px"><span class="b">User Name:</span> [[Strata Manager]]</div>
  <div class="line b" style="left:41.5px; top:219px">Buildings in Nina’s portfolio = 34</div>
  <div class="line" style="left:41.5px; top:233px"><span class="b">Brimquell Service History/General Comment Entries</span> = 127</div>
  <div class="line" style="left:41.5px; top:246px"><span class="b">Upcoming action items for all buildings in this portfolio</span> <span class="fine">(shows all ‘Next Action’ logs for today + 30 days)</span> = 15</div>
  <div class="line b" style="left:41.5px; top:259px">Overdue periodic inspections are noted against the following buildings in this portfolio:</div>
  <div class="line" style="left:41.5px; top:272.5px">Units Plan No&nbsp;&nbsp;&nbsp;&nbsp;Building Name&nbsp;&nbsp;Unit No Street No Street Name Suburb</div>
  <div class="line" style="left:41.5px; top:286px">Units Plan No&nbsp;&nbsp;&nbsp;&nbsp;Building Name&nbsp;&nbsp;Unit No Street No Street Name Suburb</div>
  <div class="line" style="left:41.5px; top:299.5px">Units Plan No&nbsp;&nbsp;&nbsp;&nbsp;Building Name&nbsp;&nbsp;Unit No Street No Street Name Suburb</div>
  <div class="line" style="left:41.5px; top:313px">Units Plan No&nbsp;&nbsp;&nbsp;&nbsp;Building Name&nbsp;&nbsp;Unit No Street No Street Name Suburb</div>
  <div class="portfolio-divider"></div>

  <div class="line" style="left:41.5px; top:340px"><span class="b">User Name:</span> [[Strata Manager]]</div>
  <div class="line b" style="left:41.5px; top:353px">Buildings in Owen’s portfolio = 34</div>
  <div class="line" style="left:41.5px; top:367px"><span class="b">Brimquell Service History/General Comment Entries</span> = 127</div>
  <div class="line" style="left:41.5px; top:380px"><span class="b">Upcoming action items for all buildings in this portfolio</span> <span class="fine">(shows all ‘Next Action’ logs for today + 30 days)</span> = 15</div>
  <div class="line b" style="left:41.5px; top:393px">Overdue periodic inspections are noted against the following buildings in this portfolio:</div>
  <div class="line" style="left:41.5px; top:407px">Units Plan No&nbsp;&nbsp;&nbsp;&nbsp;Building Name&nbsp;&nbsp;Unit No Street No Street Name Suburb</div>
  <div class="line" style="left:41.5px; top:420px">Units Plan No&nbsp;&nbsp;&nbsp;&nbsp;Building Name&nbsp;&nbsp;Unit No Street No Street Name Suburb</div>
  <div class="line" style="left:41.5px; top:433px">Units Plan No&nbsp;&nbsp;&nbsp;&nbsp;Building Name&nbsp;&nbsp;Unit No Street No Street Name Suburb</div>
  <div class="line" style="left:41.5px; top:446.5px">Units Plan No&nbsp;&nbsp;&nbsp;&nbsp;Building Name&nbsp;&nbsp;Unit No Street No Street Name Suburb</div>
  <div class="powered" style="left:213px; top:467px;"><span class="powered-label">Powered by</span><span class="brand" style="font-size:9.5px"><span class="brand-mark"></span>BRIMQUELL</span></div>
  <div class="band" style="height:10px"></div>
</section>

<!-- Building summary -->
<section class="page page-summary">
  <div class="client-logo-slot" role="img" aria-label="Space for the business's own logo"></div>
  <div class="line" style="top:86px">Building Summary</div>
  <div class="line" style="top:99.5px">UPXXXX</div>
  <div class="line" style="top:113px">Building Name</div>
  <div class="line" style="top:126.5px">Full Address</div>
  <div class="line" style="top:140px">Strata Group: Strata Group Name</div>
  <div class="line" style="top:153.5px">Strata Manager: Strata Manager Name</div>
  <div class="powered" style="left:223px; top:451px;"><span class="powered-label">Powered by</span><span class="brand"><span class="brand-mark"></span>BRIMQUELL</span></div>
  <div class="band"></div>
</section>

<!-- Insurance quotation brief -->
<section class="page page-insurance">
  <div class="client-logo-slot client-logo-slot-lg" role="img" aria-label="Space for the business's own logo"></div>
  <h1 class="title" style="top:85px; font-size:15.5px;">Insurance Quotation Brief</h1>
  <div class="line" style="top:123px">Date <span class="mark">(today’s date)</span></div>
  <div class="line" style="top:136.5px">Strata Management Group <span class="mark">(Name)</span></div>
  <div class="line" style="top:150px">Strata Manager <span class="mark">(Name – Email)</span></div>
  <div class="line" style="top:163.5px">Please find information relative to the insurance renewal application for:</div>
  <div class="line" style="top:177px"><span class="mark">Building Name &amp; Address</span></div>
  <div class="line note-red" style="top:204px">Then all this information from the Building Info page including the new fields listed on the</div>
  <div class="line note-red" style="top:212.5px">spreadsheet under Item 163</div>
  <div class="powered" style="left:213px; top:469px;"><span class="powered-label">Powered by</span><span class="brand" style="font-size:9.5px"><span class="brand-mark"></span>BRIMQUELL</span></div>
  <div class="band" style="height:11px"></div>
</section>

</body>
</html>
```